Courier Business needs a Business Card Design !!!

My new company needs a business card design. Our company name is Maple Dart Courier & Delivery Services. We will be servicing residential , government and business clients in the City of Yellowknife, Northwest Territories, Canada. I would like the following information included on the card: Name- Calvin Oxley. Title- Owner. Company- Maple Dart Courier & Delivery Services. Address- PO Box 5918 , Yellowknife , NWT, X0E 4K3. Phone- 867-555-0193. Email- mapledartdelivery@postfern.example. Facebook- www.socialpage.example/mapledartdelivery. I would like my double sided card to be the standard size of 84mm x 55mm. No borders. Use CMYK mode.1039x 697 pixels at least. I would like my logo to take up at least one quarter of the area of one side of the card. Text should be at least 8 point with perhaps my name being 10 point and my company name being 12-15 point . It should have clear readable font. Please use one or two bold colors. I am trying to attract the business community so a professional look might be best. My tag line is " On Time Every Time ". Nice safe margins please. We will be providing fast, reliable and professional delivery of envelopes and small packages within the City of Yellowknife. We offer 100% satisfaction or a complete refund. I have included a file of our logo. I like black, blue and red but am willing to look at what you feel would work best. I do not really like white as a background color.

Target Market(s)

Professionals , business owners. 30-50 years old

Industry/Entity Type

Residential

Contact Information for Business Card

As noted in brief

Font styles to use
Serif
Sans Serif

Colors
000000
0255a3
f04a50

Requirements
Must have
• My contact info. My logo
Nice to have
• Simple elegant design but still catches the eye
Should not have
• White background color

```html
<!DOCTYPE html>
<html lang="en">
<head>
<meta charset="utf-8">
<title>Maple Dart Courier &amp; Delivery Services – Business Card</title>
<link rel="stylesheet" href="https://fonts.googleapis.com/css2?family=Open+Sans:ital,wght@0,400;0,700;1,400&family=Montserrat:wght@400&display=swap">
<style>
  :root {
    --page: #ffffff;
    --card-sky: #d9edf9;
    --card-edge: #9fd3e6;
    --brand-red: #f04a50;
    --brand-blue: #0b55a5;
    --tagline-yellow: #f3e21c;
    --ink-light: #ffffff;
  }
  html, body {
    margin: 0;
    padding: 0;
    width: 1200px;
    height: 1000px;
    overflow: hidden;
    background: var(--page);
  }
  .canvas {
    position: relative;
    width: 1200px;
    height: 1000px;
  }
  .card {
    position: absolute;
    left: 108px;
    top: 178px;
    width: 996px;
    height: 645px;
    background: var(--card-sky);
    outline: 1px solid var(--card-edge);
  }
  .brand {
    position: absolute;
    left: 37px;
    top: 70px;
    margin: 0;
    font-family: "Open Sans", sans-serif;
    font-weight: 700;
    color: var(--brand-red);
    line-height: 1;
    letter-spacing: -0.5px;
  }
  .brand-name {
    display: block;
    font-size: 84px;
  }
  .brand-services {
    display: block;
    margin-top: 10px;
    font-size: 44px;
  }
  .brand-mark {
    position: absolute;
    left: 590px;
    top: 36px;
    width: 90px;
    height: 90px;
    border-radius: 50%;
    background: var(--brand-blue);
  }
  .tagline-band {
    position: absolute;
    left: -1px;
    top: 251px;
    width: 996px;
    height: 34px;
    background: var(--brand-red);
  }
  .tagline {
    position: absolute;
    left: 140px;
    top: 0;
    margin: 0;
    line-height: 34px;
    font-family: "Montserrat", sans-serif;
    font-size: 22px;
    letter-spacing: 6.4px;
    color: var(--tagline-yellow);
  }
  .person {
    position: absolute;
    left: 38px;
    top: 336px;
    margin: 0;
    font-family: "Open Sans", sans-serif;
    font-style: italic;
    color: var(--brand-blue);
    white-space: nowrap;
  }
  .person-name {
    font-size: 62px;
    letter-spacing: 0.5px;
  }
  .person-title {
    font-size: 34px;
    margin-left: 6px;
  }
  .contact-panel {
    position: absolute;
    left: 0;
    top: 422px;
    width: 998px;
    height: 223px;
    background: var(--brand-blue);
  }
  .contact-list {
    list-style: none;
    margin: 0;
    padding: 0;
    position: absolute;
    left: 39px;
    top: 35px;
    font-family: "Open Sans", sans-serif;
    font-size: 28px;
    line-height: 40px;
    color: var(--ink-light);
  }
</style>
</head>
<body>
<main class="canvas">
  <section class="card">
    <h1 class="brand">
      <span class="brand-name">MAPLE DART</span>
      <span class="brand-services">COURIER &amp; DELIVERY SERVICES</span>
    </h1>
    <span class="brand-mark" aria-hidden="true"></span>

    <div class="tagline-band">
      <p class="tagline">ON TIME EVERY TIME</p>
    </div>

    <p class="person">
      <span class="person-name">Calvin Oxley</span><span class="person-title">Owner</span>
    </p>

    <div class="contact-panel">
      <ul class="contact-list">
        <li>PO Box 5918, Yellowknife, NWT, X0E 4K3.</li>
        <li>867-555-0193</li>
        <li>mapledartdelivery@postfern.example</li>
        <li>www.socialpage.example/mapledartdelivery</li>
      </ul>
    </div>
  </section>
</main>
</body>
</html>
```